Willow Crest Website

We need a website that has clean, asian looking images that relax and motivate people to come into our integrated medical center. My current website is www.pinebrookcare.example and I would like the design for Willow Crest Health Solutions to be similar but more inviting with video content and a product purchase store as well. A moving banner would be nice too. When people are looking for ways of losing weight or getting out of pain we want them to make the connection that we have the solution. This website needs to provide sufficient information so that patients are well informed and choose us as their health provider before they ever walk through our doors. We offer comprehensive natural medicine that is based on the principles that the body can heal itself when given the right conditions. Our services include medical weight loss and hormone balancing, acupuncture and chinese herbal medicine, physical medicine, trigger point injections, allergy testing and joint rehabilitation. The Medical Doctor and Licensed Acupuncturist work as a team to provide optimal care that is catered to each individual who comes through our doors.
Updates

Target Market(s)

40 to 50 year olds who want to lose weight or have pain issues.

Industry/Entity Type

Medical

Requirements
Must have
• Use photos from our website www.pinebrookcare.example or similar content. Video content. Moving banner with relaxing images.
Nice to have
• Happy, healthy looking people. Medical Doctors working as a team. Friendly staff in a cutting edge facility.
Should not have
• Papyrus font, or big bold words.

```html
<!DOCTYPE html>
<html lang="en">
<head>
<meta charset="utf-8">
<title>Willow Crest Acupuncture</title>
<link rel="stylesheet" href="https://fonts.googleapis.com/css2?family=Ubuntu:ital,wght@0,300;0,400;0,500;1,300;1,400&display=swap">
<style>
:root{
  --olive:#5f5a2a;
  --olive-dark:#4e4a22;
  --olive-light:#7a7440;
  --backdrop:#b7b495;
  --panel:#ebe9e3;
  --ink:#333;
  --muted:#555;
  --line:#dcdcdc;
}
*{margin:0;padding:0;box-sizing:border-box}
html,body{width:994px;height:1200px;overflow:hidden;background:var(--backdrop)}
.canvas{position:absolute;left:0;top:0;width:1200px;height:1448px;transform:scale(.82834);transform-origin:0 0;font-family:'Ubuntu',sans-serif;color:var(--ink)}
.page{position:absolute;left:93px;top:0;width:1014px;height:1448px;background:#fff}
.abs{position:absolute}
.phone{right:119px;top:9px;font-size:17px;color:var(--ink)}
.phone b{font-weight:400;color:var(--olive)}
.navbar{left:88px;top:38px;width:1024px;height:46px;background:var(--olive);border-radius:3px}
.nav{left:282px;top:52px;display:flex;font-size:16px;color:#fff}
.nav span{margin-right:37px}
.brand{left:137px;top:0;width:121px;height:161px;background:#fff;padding:4px;z-index:5}
.brand-inner{width:100%;height:100%;border:2px solid var(--olive);display:flex;flex-direction:column;align-items:center;justify-content:center;gap:10px;color:var(--olive);font-size:16px;text-align:center;line-height:1.2}
.brand-inner i{width:18px;height:18px;border-radius:50%;background:var(--olive);display:block}
.banner{left:110px;top:101px;width:980px;height:343px;border-radius:22px 22px 0 0;background:linear-gradient(100deg,#dfe9f3 0%,#eef3f8 40%,#f3d9c7 65%,#e9c2a8 100%)}
.quote{left:181px;top:307px;width:411px;height:124px;background:rgba(95,90,42,.82);color:#fff;font-size:16px;font-weight:300;line-height:24px;padding:8px 11px}
.quote .by{position:absolute;right:6px;bottom:4px}
.arrow{width:67px;height:53px}
.col-title{top:455px;font-size:24px;font-weight:300;color:var(--ink);text-transform:uppercase}
.thumb{top:489px;width:295px;height:131px;border:1px solid var(--line);box-shadow:0 6px 8px -6px rgba(0,0,0,.35)}
.col-text{top:640px;width:290px;font-size:12px;line-height:18px;color:var(--muted);font-weight:300}
.btn-more{width:100px;height:23px;border-radius:12px;background:linear-gradient(#79733f,var(--olive-dark));color:#fff;font-size:11px;font-style:italic;font-weight:300;display:flex;align-items:center;justify-content:center}
.rule{left:117px;top:739px;width:964px;border-top:1px dashed #aaa}
.welcome{left:113px;top:762px;font-size:24px;font-weight:300}
.welcome em{font-style:normal;font-weight:400;color:var(--olive)}
.subhead{left:116px;top:805px;font-size:16px;font-weight:300}
.body-copy{left:116px;top:852px;width:590px;font-size:12px;line-height:24px;color:#444}
.feature{left:715px;top:766px;width:374px;height:302px;background:var(--panel)}
.feature h2{position:absolute;left:25px;top:27px;font-size:20px;font-weight:300;color:var(--olive)}
.video{left:24px;top:62px;width:330px;height:211px;background:linear-gradient(135deg,#c9956d,#e8c6a3 45%,#b77a3a 75%,#e2d36a)}
.play{left:145px;top:84px;width:50px;height:50px;border-radius:50%;background:rgba(255,255,255,.45);border:3px solid rgba(255,255,255,.7)}
.products-title{left:138px;top:1088px;font-size:20px;font-weight:300}
.products-title em{font-style:normal;font-weight:400;color:var(--olive)}
.card{top:1125px;width:209px;height:237px;border:1px solid #e3e3e3;background:#fff}
.card .pic{position:absolute;left:9px;top:9px;width:188px;height:129px}
.card .sep{position:absolute;left:0;top:148px;width:100%;border-top:1px solid #eee}
.card .name{position:absolute;left:10px;top:157px;font-family:Arial,sans-serif;font-size:12px;font-weight:bold;color:#666}
.card .desc{position:absolute;left:10px;top:172px;font-family:Arial,sans-serif;font-size:12px;color:#999}
.card .price{position:absolute;left:10px;top:197px;font-size:19px;font-style:italic;font-weight:300;color:var(--ink)}
.card .cart{position:absolute;left:112px;top:198px;width:86px;height:28px;border-radius:3px;background:var(--olive);color:#fff;font-size:12px;font-weight:300;display:flex;align-items:center;justify-content:center}
.footer{left:93px;top:1390px;width:1014px;height:58px;background:var(--olive);color:#fff}
.foot-links{left:22px;top:10px;font-size:13px}
.foot-links span{margin:0 7px}
.copy{left:22px;top:34px;font-size:11px;font-weight:300}
.follow{left:760px;top:22px;font-size:16px;font-weight:300}
.social{top:18px;width:25px;height:25px;border-radius:2px}
</style>
</head>
<body>
<div class="canvas">
  <div class="page"></div>

  <div class="abs phone"><b>(555)</b> 201-4410 <span>or</span> <b>(555)</b> 307-2286</div>

  <div class="abs navbar"></div>
  <nav class="abs nav">
    <span>So Tai Ho</span><span>Seitai Shinpo</span><span>Acupuncture</span><span>Biography</span><span>Nutrition</span><span>My Journey</span><span>Contant Us</span>
  </nav>

  <div class="abs banner" role="img" aria-label="Banner photo: relaxed patient receiving facial acupuncture needles"></div>
  <svg class="abs arrow" style="left:98px;top:265px" viewBox="0 0 67 53"><polygon points="0,0 8,4 67,4 67,53 0,50" fill="var(--olive-light)"/><polyline points="38,14 26,28 38,42" fill="none" stroke="#fff" stroke-width="1.5"/></svg>
  <svg class="abs arrow" style="left:1034px;top:193px" viewBox="0 0 67 53"><polygon points="0,4 60,4 67,0 67,50 0,53" fill="var(--olive-light)"/><polyline points="29,14 41,28 29,42" fill="none" stroke="#fff" stroke-width="1.5"/></svg>
  <div class="abs quote">"The Doctor of the future will give no medicine but will interest patients in the care of the human frame, in diet, and &nbsp;in the cause and prevention of disease."<span class="by">Harold Linwick</span></div>

  <div class="abs brand"><div class="brand-inner"><i></i>Willow<br>Crest</div></div>

  <h2 class="abs col-title" style="left:118px">So Thi Ho</h2>
  <h2 class="abs col-title" style="left:456px">Seitai Shinpo</h2>
  <h2 class="abs col-title" style="left:795px">Acupuncture</h2>

  <div class="abs thumb" style="left:112px;background:linear-gradient(100deg,#f4e0d2,#c98b66 50%,#f6eee8)" role="img" aria-label="Photo: woman receiving a shoulder massage"></div>
  <div class="abs thumb" style="left:451px;background:linear-gradient(100deg,#dde8f2,#eef2f6 50%,#eac4aa)" role="img" aria-label="Photo: patient with acupuncture needles in forehead"></div>
  <div class="abs thumb" style="left:790px;background:linear-gradient(100deg,#f1efec,#e6ddd4 45%,#e0b99a)" role="img" aria-label="Photo: practitioner treating a smiling patient"></div>

  <p class="abs col-text" style="left:116px">Sotai ho is a system of movement therapy that was discovered after nearly 10 years of personal research from Kenji Morimura, M.D. (1897-1993)</p>
  <p class="abs col-text" style="left:455px">Seitai Shinpo is a system of acupuncture developed by Dr. Hiro Tanabe in the 1970s. He was the first to discover that internal organ systems ..</p>
  <p class="abs col-text" style="left:794px">While pursuing a degree in premedicine &amp; behavior science at the university, Marin learned the benefits of Chinese medicine while taking a History of Medicine..</p>

  <div class="abs btn-more" style="left:115px;top:702px">Learn More...</div>
  <div class="abs btn-more" style="left:458px;top:702px">Learn More...</div>
  <div class="abs btn-more" style="left:795px;top:702px">Learn More...</div>

  <div class="abs rule"></div>

  <h1 class="abs welcome">Welcome to <em>Willow Crest Acupuncture</em></h1>
  <h3 class="abs subhead">How does acupuncture work?</h3>
  <p class="abs body-copy">As the needles are carefully inserted into acupuncture points, specific cells stimulate nerve pathways that trigger a healing response to a particular organ system or area of the body. &nbsp;Acupuncture also acts on the autonomic nervous system and causes the release of endorphins, enkephalins and other natural pain relieving chemicals. &nbsp;At Willow Crest Acupuncture the system of acupuncture used is called Seitai Shinpo (which translates into “correct posture acupuncture method”) that uses acupuncture and moxibustion to balance structural distortions by releasing tense areas of contraction along the spine. &nbsp;When the structure is properly balanced then the body will heal much quicker.</p>
  <div class="abs btn-more" style="left:113px;top:1031px">Learn More...</div>

  <section class="abs feature">
    <h2>Featured Video</h2>
    <div class="abs video" role="img" aria-label="Video still: spa massage with oils and flowers">
      <div class="abs play"><svg width="44" height="44" viewBox="0 0 44 44"><polygon points="16,14 32,22 16,30" fill="#6a6440"/></svg></div>
    </div>
  </section>

  <h2 class="abs products-title">Our <em>Products</em></h2>

  <div class="abs card" style="left:137px"><div class="pic" role="img" aria-label="Product photo: green candles and white towels" style="background:linear-gradient(135deg,#dfe8d6,#c6d98a 55%,#eef0e6)"></div><div class="sep"></div><div class="name">Lorem ipsum dolor sit ame</div><div class="desc">Consectetuer elit....</div><div class="price">$30.99</div><div class="cart">Add to cart</div></div>
  <div class="abs card" style="left:375px"><div class="pic" role="img" aria-label="Product photo: lavender, lemon and oil bottle" style="background:linear-gradient(135deg,#e9dcc6,#9b8db4 45%,#d8b67a)"></div><div class="sep"></div><div class="name">Lorem ipsum dolor sit ame</div><div class="desc">Consectetuer elit....</div><div class="price">$25.99</div><div class="cart">Add to cart</div></div>
  <div class="abs card" style="left:610px"><div class="pic" role="img" aria-label="Product photo: rolled towels and lit candles" style="background:linear-gradient(135deg,#6a3b22,#c9a78a 45%,#c8482a)"></div><div class="sep"></div><div class="name">Lorem ipsum dolor sit ame</div><div class="desc">Consectetuer elit....</div><div class="price">$35.99</div><div class="cart">Add to cart</div></div>
  <div class="abs card" style="left:844px"><div class="pic" role="img" aria-label="Product photo: white flower with oil bowl" style="background:linear-gradient(135deg,#f1ead8,#4d7a32 45%,#c8823a)"></div><div class="sep"></div><div class="name">Lorem ipsum dolor sit ame</div><div class="desc">Consectetuer elit....</div><div class="price">$50.99</div><div class="cart">Add to cart</div></div>

  <footer class="abs footer">
    <div class="abs foot-links">So Tai Ho<span>|</span>Seitai Shinpo<span>|</span>Acupuncture<span>|</span>Biography<span>|</span>Nutrition<span>|</span>My Journey<span>|</span>Contact Us</div>
    <div class="abs copy">Copyright 2012 © Willow Crest Acupuncture — All Rights Reserved</div>
    <div class="abs follow">Follow us on:</div>
    <div class="abs social" style="left:862px;background:#e8892a"></div>
    <div class="abs social" style="left:894px;background:#3b5998"></div>
    <div class="abs social" style="left:926px;background:#3fa9d8"></div>
    <div class="abs social" style="left:961px;background:#2a77a8"></div>
  </footer>
</div>
</body>
</html>
```